Economics of an Assumption vs Obtaining a New Loan at Current Market Rate

I need to marketing flyer that has fields that calculate mortgage payments amongst other calculations. I have a rough draft that I will attach.

The idea is to provide a tool for a real estate agent to use to illustrate to a potential buyer what a payment would be if they assumed the existing loan on the house or took out a new loan at current market.

The flyer needs to be able to allow an agent to drop in their logo, photo, and contact along with the loan officers photo and contact info.

You can google open house flyer to see examples of what the overall artwork and presentation can look like.

Target Market(s)

Home Buyers

Industry/Entity Type

Real Estate

Colors
F0912C
F2A743
F7CA91
FBE8D2
FDF5EE
EE7325
F08F49
F5BC92
FAE3D3
FDF4ED

Requirements
Must have
• A way to calculate mortgage payment
Nice to have
• Photo and logo drop ins

```html
<!DOCTYPE html>
<html lang="en">
<head>
<meta charset="utf-8">
<title>Nestora – Assumption vs New Loan Flyer</title>
<link href="https://fonts.googleapis.com/css2?family=Source+Sans+3:wght@400;600;700&family=Yellowtail&display=swap" rel="stylesheet">
<style>
  :root{
    --orange:#F0912C;
    --orange-deep:#EE7325;
    --orange-soft:#F2A743;
    --page:#FBF9FC;
    --ink:#1f1f1f;
    --box-line:#222;
    --white:#ffffff;
  }
  *{box-sizing:border-box;margin:0;padding:0}
  html,body{width:848px;height:1200px;overflow:hidden;background:var(--page)}
  .flyer{position:relative;width:848px;height:1200px;background:var(--page);font-family:"Source Sans 3",Arial,sans-serif;color:var(--ink);overflow:hidden}
  .hero{position:absolute;left:0;top:0;width:848px;height:460px}
  .abs{position:absolute}
  .brand{position:absolute;left:24px;top:44px;display:flex;align-items:center;gap:8px;font-weight:400;font-size:48px;color:var(--orange-deep);letter-spacing:1px}
  .brand-dot{width:18px;height:18px;border-radius:50%;background:var(--orange-deep)}
  .price-label{left:168px;top:481px;font-size:29px;font-weight:700;letter-spacing:4px;color:var(--orange)}
  .price-box{left:487px;top:482px;width:185px;height:35px;border:2px solid var(--box-line);border-radius:5px;background:var(--white)}
  .section-title{font-size:25px;font-weight:700;color:var(--orange);letter-spacing:.3px;border-bottom:2px solid var(--orange);line-height:27px;white-space:nowrap}
  .row-label{font-size:24.5px;line-height:26px;color:var(--ink);white-space:nowrap}
  .colon{font-size:22px;line-height:24px}
  .field{height:24px;border:1.5px solid var(--box-line);background:var(--white);font-size:16px;line-height:21px;padding-left:10px;white-space:nowrap;color:var(--ink)}
  .field.center{text-align:center;padding-left:0}
  .field small{font-size:9.5px;line-height:8px;display:inline-block;vertical-align:middle}
  .diff-label{left:128px;top:822px;font-size:29px;font-weight:700;letter-spacing:4px;color:var(--orange)}
  .tagline{left:108px;top:864px;font-size:30px;font-weight:700;color:var(--ink);white-space:nowrap}
  .tagline .script{font-family:"Yellowtail",cursive;font-weight:400;font-size:40px;margin-left:16px}
  .footer{position:absolute;left:0;top:934px;width:848px;height:266px;background:var(--orange)}
  .card{position:absolute;top:18px;height:229px;border-radius:14px;background:var(--white)}
  .photo-card{left:48px;width:183px;padding:4px}
  .logo-card{left:254px;width:184px;display:flex;align-items:center;justify-content:center;gap:6px;font-size:34px;color:var(--orange-deep)}
  .logo-card .brand-dot{width:13px;height:13px}
  .quote-pill{position:absolute;left:484px;top:22px;width:364px;height:49px;background:var(--white);border-radius:25px 0 0 25px;font-size:20.5px;font-weight:700;color:var(--orange-deep);line-height:49px;padding-left:19px;white-space:nowrap}
  .contact{position:absolute;left:493px;display:flex;align-items:center;gap:16px;color:var(--white);font-size:20px;white-space:nowrap}
  .contact b{font-weight:700}
  .contact svg{flex:none}
</style>
</head>
<body>
<div class="flyer">

  <svg class="hero" viewBox="0 0 848 460">
    <defs>
      <linearGradient id="sky" x1="0" y1="0" x2="0" y2="1">
        <stop offset="0" stop-color="#7f8fb3"/>
        <stop offset=".4" stop-color="#a99fb4"/>
        <stop offset=".55" stop-color="#b88a60"/>
        <stop offset=".85" stop-color="#a97d56"/>
        <stop offset="1" stop-color="#b4aba4"/>
      </linearGradient>
    </defs>
    <rect width="848" height="456" fill="url(#sky)" role="img" aria-label="Photo of the listed stucco house with tile roof"/>
    <path d="M0 0 H282 Q200 150 0 174 Z" fill="var(--white)"/>
    <path d="M282 0 Q200 150 0 174" fill="none" stroke="var(--orange)" stroke-width="4"/>
    <polygon points="489,456 670,326 848,452 848,460 0,460 0,456" fill="var(--page)"/>
    <line x1="0" y1="454" x2="492" y2="454" stroke="var(--orange)" stroke-width="5"/>
    <polyline points="489,456 670,326 848,452" fill="none" stroke="var(--orange)" stroke-width="6"/>
  </svg>

  <div class="brand"><span class="brand-dot"></span>Nestora</div>

  <div class="abs price-label">PURCHASE PRICE :</div>
  <div class="abs price-box"></div>

  <!-- Current mortgage -->
  <div class="abs section-title" style="left:15px;top:547px;width:269px">CURRENT MORTGAGE :</div>
  <div class="abs row-label" style="left:21px;top:594px">Loan ammount</div>
  <div class="abs row-label" style="left:21px;top:623px">Interest rate</div>
  <div class="abs row-label" style="left:21px;top:651px">Principal 3 interest</div>
  <div class="abs row-label" style="left:21px;top:679px">Mortgage Insurance:</div>
  <div class="abs row-label" style="left:21px;top:708px">Total</div>
  <div class="abs colon" style="left:226px;top:596px">:</div>
  <div class="abs colon" style="left:226px;top:625px">:</div>
  <div class="abs colon" style="left:226px;top:653px">:</div>
  <div class="abs colon" style="left:226px;top:710px">:</div>
  <div class="abs field center" style="left:244px;top:596px;width:108px">Allow Input</div>
  <div class="abs field center" style="left:244px;top:624px;width:108px">Allow Input</div>
  <div class="abs field center" style="left:244px;top:652px;width:108px">Allow Input</div>
  <div class="abs field center" style="left:244px;top:680px;width:108px">Allow Input</div>
  <div class="abs field" style="left:244px;top:709px;width:108px"></div>
  <div class="abs row-label" style="left:21px;top:736px">Years</div>
  <div class="abs field" style="left:83px;top:738px;width:61px"></div>
  <div class="abs row-label" style="left:152px;top:737px">Months</div>
  <div class="abs field" style="left:244px;top:738px;width:60px"></div>
  <div class="abs row-label" style="left:21px;top:768px">Delta</div>
  <div class="abs field center" style="left:83px;top:769px;width:267px;font-size:15px">Purchase price minus lean amount</div>

  <!-- New mortgage -->
  <div class="abs section-title" style="left:392px;top:547px;width:431px">NEW MORTGAGE 10% DOWN PAYMENT</div>
  <div class="abs row-label" style="left:397px;top:594px">Loan ammount</div>
  <div class="abs row-label" style="left:397px;top:623px">Interest rate</div>
  <div class="abs row-label" style="left:397px;top:651px">Principal 3 interest</div>
  <div class="abs row-label" style="left:397px;top:679px">Mortgage Insurance:</div>
  <div class="abs row-label" style="left:397px;top:708px">Total</div>
  <div class="abs colon" style="left:602px;top:596px">:</div>
  <div class="abs colon" style="left:602px;top:625px">:</div>
  <div class="abs colon" style="left:602px;top:653px">:</div>
  <div class="abs colon" style="left:602px;top:710px">:</div>
  <div class="abs field" style="left:620px;top:596px;width:204px;padding-left:17px">90% of purchase price</div>
  <div class="abs field" style="left:620px;top:624px;width:204px;padding-left:17px">Input</div>
  <div class="abs field" style="left:620px;top:653px;width:204px;padding-left:17px">Calc payment</div>
  <div class="abs field" style="left:620px;top:681px;width:204px;padding-left:17px">Input %</div>
  <div class="abs field" style="left:620px;top:709px;width:204px;padding-left:17px;font-size:15px">Principal interest + <small>Mortgage<br>Insurance</small></div>
  <div class="abs row-label" style="left:397px;top:736px">Term</div>
  <div class="abs field center" style="left:459px;top:736px;width:62px">Input</div>
  <div class="abs row-label" style="left:528px;top:737px">Years</div>
  <div class="abs row-label" style="left:397px;top:767px">Down payment amount</div>
  <div class="abs field" style="left:653px;top:769px;width:60px"></div>

  <div class="abs diff-label">PAYMENT DIFFERENCE :</div>
  <div class="abs field center" style="left:526px;top:825px;width:196px;height:30px;line-height:27px">Difference Between totals</div>

  <div class="abs tagline">This property is “<span class="script">Locked Low Rate Ready</span> ”</div>

  <footer class="footer">
    <div class="card photo-card">
      <svg width="175" height="221" viewBox="0 0 175 221" role="img" aria-label="Agent or property photo">
        <defs>
          <linearGradient id="thumb" x1="0" y1="0" x2="0" y2="1">
            <stop offset="0" stop-color="#7f8fb3"/>
            <stop offset=".35" stop-color="#a99fb4"/>
            <stop offset=".55" stop-color="#b0845c"/>
            <stop offset="1" stop-color="#b7b0aa"/>
          </linearGradient>
        </defs>
        <rect width="175" height="221" rx="11" fill="url(#thumb)"/>
      </svg>
    </div>
    <div class="card logo-card"><span class="brand-dot"></span>Nestora</div>

    <div class="quote-pill">For a FREE Quote Please Contact Us:</div>

    <div class="contact" style="top:82px">
      <svg width="26" height="26" viewBox="0 0 26 26"><circle cx="13" cy="13" r="12" fill="none" stroke="#fff" stroke-width="1.5"/><path d="M9 7.5c1 0 1.6 2.2 1.6 2.6 0 .6-1 1-1 1.6.4 1.6 2.2 3.5 3.8 3.9.6 0 1-1 1.6-1 .4 0 2.6.6 2.6 1.6 0 1-1.3 2.3-2.4 2.3-3.8 0-8.5-4.7-8.5-8.5C6.7 8.8 8 7.5 9 7.5z" fill="#fff"/></svg>
      <span>OFFICE &nbsp;: <b>0123456789</b></span>
    </div>
    <div class="contact" style="top:120px">
      <svg width="26" height="26" viewBox="0 0 26 26"><circle cx="13" cy="13" r="12" fill="none" stroke="#fff" stroke-width="1.5"/><path d="M9 7.5c1 0 1.6 2.2 1.6 2.6 0 .6-1 1-1 1.6.4 1.6 2.2 3.5 3.8 3.9.6 0 1-1 1.6-1 .4 0 2.6.6 2.6 1.6 0 1-1.3 2.3-2.4 2.3-3.8 0-8.5-4.7-8.5-8.5C6.7 8.8 8 7.5 9 7.5z" fill="#fff"/></svg>
      <span>MOBILE : <b>0123456789</b></span>
    </div>
    <div class="contact" style="top:159px">
      <svg width="26" height="26" viewBox="0 0 26 26"><circle cx="13" cy="13" r="12" fill="none" stroke="#fff" stroke-width="1.5"/><g fill="none" stroke="#fff" stroke-width="1.2"><circle cx="13" cy="13" r="7"/><ellipse cx="13" cy="13" rx="3" ry="7"/><line x1="6" y1="13" x2="20" y2="13"/><line x1="7" y1="9.5" x2="19" y2="9.5"/><line x1="7" y1="16.5" x2="19" y2="16.5"/></g></svg>
      <span>www.<b>yourwebsite</b>.com</span>
    </div>
    <div class="contact" style="top:198px">
      <svg width="26" height="26" viewBox="0 0 26 26"><circle cx="13" cy="13" r="12" fill="none" stroke="#fff" stroke-width="1.5"/><path d="M7 11l6-4 6 4v7H7z" fill="#fff"/><path d="M7 11l6 4 6-4" fill="none" stroke="var(--orange)" stroke-width="1"/></svg>
      <span>youremailhere@example.com</span>
    </div>
  </footer>
</div>
</body>
</html>
```